Renewed electronic office supplies

I need a landing page design for a B2B business that will sell refurbished and renewed electronic devices such as smartphones, laptops, tablets and other gadgets. We want to become suppliers of these devices to companies that need computers and other devices for their employees. The point of our business is that they can get a great device that is in very good contrition instead of buying brand new. Companies will be able to save 50-60% on these renewed devices. Not only that we will also buy the companies old devices which they no longe needs and renew them and give them new life so we can resell it.

Our services will be:

- sale of renewed devices with lifetime warranty

- purchase of old devices

- swap solution: meaning client buy from us and sell at the same time so we deduct the amount sale of their old devices into their purchase.

Some useful information:

- company name and logo are still pending

- we aim to provide all business with top quality of renewed and environmentally friendly electronics, while maintaining a minimal impact on the natural environment.

I have attached a word document with some additional info that might be useful

Looking forward to seeing all your great designs!

P.s. Please feel free to make designs that are not based on my documents also, we need different layouts and designs. as for now I see many of the designs are more or less the same. we need more variation on design
Updates

Target Market(s)

Medium to large Businesses

Industry/Entity Type

Technology Equipment

Requirements
Must have
• we need more designs to be submitted , 50 designs minimum

```html
<!DOCTYPE html>
<html lang="en">
<head>
<meta charset="utf-8">
<title>Renewa Supply Co — Reusable Electronic Office Supplies</title>
<link href="https://fonts.googleapis.com/css2?family=Poppins:wght@300;400;500;600;700&display=swap" rel="stylesheet">
<style>
:root{
  --green:#2fe39b;
  --navy:#1b2a3c;
  --hero-blue:#1f4868;
  --hero-deep:#17324b;
  --ink:#1d1d1f;
  --muted:#8a8f96;
  --footer:#141414;
  --white:#ffffff;
  --soft:#eef0f2;
}
*{margin:0;padding:0;box-sizing:border-box}
html,body{width:1200px;height:3992px;overflow:hidden}
body{font-family:'Poppins',sans-serif;color:var(--ink);background:var(--white);position:relative}
.abs{position:absolute}
.btn{position:absolute;display:flex;align-items:center;justify-content:center;background:var(--green);color:var(--white);font-weight:600;font-size:15px;border-radius:24px;text-decoration:none}
.photo{position:absolute;overflow:hidden}

/* hero */
.hero-shape{position:absolute;left:0;top:0}
.brand{position:absolute;left:88px;color:var(--white)}
.brand-name{font-weight:700;font-size:31px;line-height:1;letter-spacing:.5px}
.brand-sub{font-weight:400;font-size:13px;letter-spacing:11.5px;margin-top:6px}
.nav{position:absolute;top:48px;left:573px;display:flex;gap:58px;font-size:15px;color:var(--white)}
.nav .active{color:var(--green)}
.hero-title{position:absolute;left:88px;top:126px;font-size:48px;font-weight:700;line-height:50px;color:var(--white)}
.hero-text{position:absolute;left:88px;top:243px;width:560px;font-size:15.5px;font-weight:300;line-height:31px;color:var(--white)}

/* categories */
.cat{position:absolute;top:740px;width:272px;height:273px;border-radius:32px;overflow:hidden}
.cat-label{position:absolute;bottom:18px;left:0;right:0;text-align:center;color:var(--white);font-weight:700;font-size:22px}

/* about */
.about-kicker{position:absolute;left:608px;top:1108px;font-size:16px;color:#555}
.about-title{position:absolute;left:608px;top:1132px;font-size:34px;font-weight:700;line-height:39px}
.about-text{position:absolute;left:608px;top:1226px;width:502px;font-size:15.5px;font-weight:300;line-height:31.3px;color:#6d7278;text-align:justify}

/* savings banner */
.banner{position:absolute;left:0;top:1582px;width:1200px;height:338px;background:var(--navy)}
.save{position:absolute;left:0;right:0;top:88px;text-align:center;color:var(--white);font-size:24px;font-weight:300}
.save b{font-size:68px;font-weight:700;vertical-align:-6px;margin:0 4px}

/* services */
.section-title{position:absolute;left:0;right:0;text-align:center;font-size:38px;font-weight:700}
.service{position:absolute;top:2090px;text-align:center;font-size:14px;font-weight:300;line-height:23.3px;color:var(--muted)}
.service svg{display:block;margin:0 auto 12px}

/* news */
.news{position:absolute;top:3093px;width:333px;height:377px;border-radius:34px;overflow:hidden}
.news-tag{position:absolute;top:228px;left:0;right:0;text-align:center;color:var(--white);font-size:17px;font-weight:300}
.news-title{position:absolute;top:260px;left:0;right:0;text-align:center;color:var(--white);font-size:22px;font-weight:600;line-height:32px}

/* footer */
.footer{position:absolute;left:0;top:3570px;width:1200px;height:422px;background:var(--footer);color:var(--white)}
.f-head{position:absolute;top:106px;font-size:19px;font-weight:600}
.f-list{position:absolute;top:160px;font-size:14px;font-weight:300;line-height:29.5px}
.social{position:absolute;left:88px;top:196px;display:flex;gap:38px}
.social span{width:12px;height:12px;border-radius:50%;background:var(--white)}
.f-input{position:absolute;left:857px;top:163px;width:253px;height:42px;background:var(--white);color:#888;font-size:13px;padding:12px 18px}
.f-sub{position:absolute;left:857px;top:212px;width:253px;height:42px;background:var(--green);color:var(--white);font-size:13px;display:flex;align-items:center;justify-content:center}
.copy{position:absolute;left:0;right:0;top:386px;text-align:center;font-size:12px}
</style>
</head>
<body>

<!-- hero -->
<svg class="hero-shape" width="1200" height="660" viewBox="0 0 1200 660">
  <defs>
    <linearGradient id="heroFill" x1="0" y1="0" x2="1" y2="1">
      <stop offset="0" stop-color="#2a5a7e"/>
      <stop offset=".6" stop-color="#1f4868"/>
      <stop offset="1" stop-color="#163049"/>
    </linearGradient>
  </defs>
  <path d="M390 640 Q470 655 560 610 L1200 240 V300 L620 640 Z" fill="#eef0f2"/>
  <path d="M0 0 H1200 V165 L570 580 Q470 640 370 610 Q290 590 220 500 L0 150 Z" fill="url(#heroFill)" role="img" aria-label="Technician repairing a circuit board, tinted blue"/>
</svg>
<div class="photo" style="left:680px;top:155px;width:245px;height:475px;border-radius:36px;background:linear-gradient(160deg,#f3f4f6,#cfd3d8);transform:rotate(12deg)" role="img" aria-label="White smartphone with a cracked screen"></div>

<div class="brand" style="top:20px"><div class="brand-name">RENEWA SUPPLY</div><div class="brand-sub">COMPANY</div></div>
<nav class="nav"><span class="active">Home</span><span>Services</span><span>Blog</span><span>About Us</span><span>Contact Us</span></nav>
<h1 class="hero-title">Reusable Electronic<br>Office Supplies</h1>
<p class="hero-text">we aim to provide all business with top quality of reused and environmentally friendly electronics, while maintaining a minimal impact on the natural environment.</p>
<a class="btn" style="left:88px;top:362px;width:130px;height:46px">Shop</a>

<!-- categories -->
<div class="cat" style="left:45px;background:linear-gradient(160deg,#3d5f7a,#15293c)" role="img" aria-label="Smartphone being repaired"><div class="cat-label">Smart phones</div></div>
<div class="cat" style="left:324px;background:linear-gradient(160deg,#4a6a84,#182d40)" role="img" aria-label="Laptop being repaired"><div class="cat-label">Laptops</div></div>
<div class="cat" style="left:604px;background:linear-gradient(160deg,#5a7890,#1a3044)" role="img" aria-label="Tablet being repaired"><div class="cat-label">Tablets</div></div>
<div class="cat" style="left:884px;background:linear-gradient(160deg,#34546e,#142638)" role="img" aria-label="Technician working on gadgets"><div class="cat-label">Gadgets</div></div>

<!-- about -->
<div class="photo" style="left:155px;top:1116px;width:378px;height:356px;background:linear-gradient(90deg,#1e1a17 0 47%,#fff 47% 53%,#1a1817 53%);border-radius:14px" role="img" aria-label="Two black smartphones, one with a cracked screen"></div>
<div class="about-kicker">We are</div>
<h2 class="about-title">A smarter circular solution<br>for electronic supplies</h2>
<p class="about-text">Billions of electronics are being made, sold, and disposed of every year – a cycle that drives short-term profits for electronics manufacturers, but at too high a cost for the planet we all share. With our experience in the recycling market we can put an end to this cycle and offer a circular solution that is both affordable and environmentally friendly.</p>
<a class="btn" style="left:608px;top:1436px;width:147px;height:46px">Read More</a>

<!-- savings banner -->
<section class="banner">
  <div class="save">Save <b>50-60%</b> on these renewed devices</div>
  <a class="btn" style="left:527px;top:191px;width:147px;height:46px">Shop Now</a>
</section>

<!-- services -->
<h2 class="section-title" style="top:2008px">Our Services</h2>
<div class="service" style="left:88px;width:180px">
  <svg width="66" height="66" viewBox="0 0 66 66" fill="none" stroke="#1d1d1f" stroke-width="2"><rect x="14" y="4" width="36" height="50" rx="3"/><circle cx="32" cy="20" r="9"/><path d="M28 24l8-8M28 17h.1M36 23h.1M20 38h22M20 44h16"/><circle cx="48" cy="50" r="10"/><path d="M48 45v10M45 48h5a2 2 0 010 4h-4"/><path d="M6 56h30"/></svg>
  Sale of renewed devices<br>with lifetime warranty
</div>
<div class="service" style="left:326px;width:180px">
  <svg width="66" height="66" viewBox="0 0 66 66" fill="none" stroke="#1d1d1f" stroke-width="2"><rect x="20" y="4" width="26" height="58" rx="4"/><rect x="25" y="14" width="16" height="14"/><path d="M27 36h.1M33 36h.1M39 36h.1M27 43h.1M33 43h.1M39 43h.1M27 50h.1M33 50h.1M39 50h.1"/></svg>
  Purchase of old devices
</div>
<div class="service" style="left:554px;width:240px">
  <svg width="66" height="66" viewBox="0 0 66 66" fill="none" stroke="#1d1d1f" stroke-width="2"><circle cx="12" cy="10" r="6"/><path d="M22 8h20l-4-4M42 12H22l4 4"/><circle cx="54" cy="10" r="5"/><path d="M14 30h10l-6 10h6M18 40v20M44 30h10M48 30v30M44 40h8M44 50h8"/></svg>
  Swap solution: meaning<br>clients buy from us and sell at the<br>same time so we deduct the<br>amount sale of their old devices<br>into their purchase.
</div>
<div class="service" style="left:842px;width:270px">
  <svg width="66" height="66" viewBox="0 0 66 66" fill="none" stroke="#1d1d1f" stroke-width="2"><path d="M33 36V18M33 26c-6 0-10-4-10-10 6 0 10 4 10 10zM33 22c0-6 4-10 10-10 0 6-4 10-10 10z"/><path d="M6 20l2 22 12 16M60 20l-2 22-12 16M14 30l6 12 6 6M52 30l-6 12-6 6"/></svg>
  We aim to provide all<br>businesses with top quality of<br>renewed and environmentally friendly<br>electronics, while maintaining a<br>minimal impact on the natural<br>environment.
</div>

<!-- video -->
<div class="photo" style="left:0;top:2420px;width:1200px;height:515px;background:linear-gradient(90deg,#b88a52 0%,#d8cfc2 40%,#e9e6e0 70%,#9aa38a 100%)" role="img" aria-label="Smiling man working on a laptop at a desk with plants"></div>
<svg class="abs" style="left:558px;top:2637px" width="84" height="84" viewBox="0 0 84 84"><circle cx="42" cy="42" r="38" fill="none" stroke="#fff" stroke-width="5"/><path d="M33 26l24 16-24 16z" fill="#fff"/></svg>

<!-- news -->
<h2 class="section-title" style="top:3025px">Latest News</h2>
<div class="news" style="left:90px;background:linear-gradient(170deg,#efe9e4,#8a7a6e 70%,#4d423a)" role="img" aria-label="Woman smiling at her smartphone"><div class="news-tag">Product Review</div><div class="news-title">Lorem ipsum dolor<br>sit amet, consectetur<br>adipiscing elit</div></div>
<div class="news" style="left:434px;background:linear-gradient(170deg,#e3e5e8,#6a6e74 60%,#1d1f22)" role="img" aria-label="Keyboard, mouse and headphones on a desk"><div class="news-tag">Product Review</div><div class="news-title">Lorem ipsum dolor<br>sit amet, consectetur<br>adipiscing elit</div></div>
<div class="news" style="left:778px;background:linear-gradient(170deg,#f1e6dc,#b7967f 60%,#6b5446)" role="img" aria-label="Hand holding a smartphone"><div class="news-tag">Product Review</div><div class="news-title">Lorem ipsum dolor<br>sit amet, consectetur<br>adipiscing elit</div></div>

<!-- footer -->
<footer class="footer">
  <div class="brand" style="top:100px"><div class="brand-name">RENEWA SUPPLY</div><div class="brand-sub">COMPANY</div></div>
  <div class="social"><span></span><span></span><span></span><span></span><span></span></div>
  <div class="f-head" style="left:433px">Links</div>
  <div class="f-list" style="left:433px">Home<br>Services<br>Blog<br>About Us<br>Contact Us</div>
  <div class="f-head" style="left:590px">Contact Us</div>
  <div class="f-list" style="left:590px">Lorem ipsum dolor sit amet,<br>consectetur<br>+ 1 555 014 2290<br>info@renewasupply.com</div>
  <div class="f-head" style="left:856px">Newsletter</div>
  <div class="f-input">Your Email Address</div>
  <div class="f-sub">Subscribe</div>
  <div class="copy">© 2020 The Company Name. All Rights Reserved.</div>
</footer>

</body>
</html>
```